exquisite label design for foam cleanser

Kindly invite you to design bottle label (102 mm*64 mm) for our product, a kind of foam cleanser for wearable aligners. The color of bottle and liquid inside are both clear, but the foam pump is white. You could download the pic of bottle among the uploaded files. I have no KV of our website or posters to supply you, except the logo file attached. Content on the label is attached too. Please check it. I wish the label would make our product look high-end and reliable. And it would be better if you could give some advice on paper material and special requirements for printing, related to your design. I value the texture of label too, because I think that stands for the quality of products. No color limitation for the use of our logo, and please ignore the Chinese characters in our logo, they are not in our plan.
Target Market(s)
16-35 female, orthodontic patients.
Colors
Designer to choose colors to be used in the design.
Look and feel
Each slider illustrates characteristics of the customer's brand and the style your logo design should communicate.

```html
<!DOCTYPE html>
<html lang="en">
<head>
<meta charset="utf-8">
<title>Aligner Cleaning Foam Label</title>
<link rel="stylesheet" href="https://fonts.googleapis.com/css2?family=Cabin:wght@500;600;700&family=Noto+Sans+TC:wght@500&display=swap">
<style>
  :root {
    --page: #f3f3f4;
    --sky-edge: #4aaddf;
    --sky-mid: #a9e1f6;
    --paper: #ffffff;
    --accent: #2b9fd8;
    --ink: #1e1e1e;
  }
  * { margin: 0; padding: 0; box-sizing: border-box; }
  html, body {
    width: 1200px;
    height: 1200px;
    overflow: hidden;
    background: var(--page);
  }
  .label {
    position: absolute;
    left: 351px;
    top: 60px;
    width: 498px;
    height: 1080px;
    display: flex;
    flex-direction: column;
    border-radius: 10px;
    overflow: hidden;
    font-family: "Cabin", sans-serif;
    text-align: center;
  }
  .band-sky {
    background: linear-gradient(90deg, var(--sky-edge) 0%, var(--sky-mid) 50%, var(--sky-edge) 100%);
  }
  .band-paper { background: var(--paper); }

  .hero {
    height: 514px;
    position: relative;
  }
  .brand-name {
    position: absolute;
    top: 150px;
    left: 0;
    right: 0;
    font-weight: 700;
    font-size: 92px;
    letter-spacing: 2px;
    color: var(--paper);
  }
  .product-cn {
    position: absolute;
    top: 388px;
    left: 0;
    right: 0;
    font-family: "Noto Sans TC", sans-serif;
    font-weight: 500;
    font-size: 40px;
    color: var(--ink);
    letter-spacing: 1px;
  }

  .claims {
    height: 218px;
    display: flex;
    flex-direction: column;
    justify-content: center;
    color: var(--accent);
    font-weight: 700;
  }
  .claim-main { font-size: 51px; line-height: 1.05; }
  .claim-amp { font-size: 50px; line-height: 1.2; }
  .claim-sub { font-size: 38px; line-height: 1.1; }

  .flavor {
    height: 237px;
    display: flex;
    align-items: center;
    justify-content: center;
    font-weight: 700;
    font-size: 41px;
    color: var(--ink);
  }
  .volume {
    height: 46px;
    display: flex;
    align-items: center;
    justify-content: center;
    font-weight: 700;
    font-size: 28px;
    color: var(--ink);
  }
  .footer { height: 65px; }
</style>
</head>
<body>
  <main class="label">
    <section class="hero band-sky">
      <div class="brand-name">Clariva</div>
      <div class="product-cn">隱形牙套清潔泡沫</div>
    </section>
    <section class="claims band-paper">
      <div class="claim-main">DEEP CLEANING</div>
      <div class="claim-amp">&amp;</div>
      <div class="claim-sub">LASTING FRESHNESS</div>
    </section>
    <section class="flavor band-sky">MINT FLAVOR</section>
    <section class="volume band-paper">1.69 FL OZ / 50ML</section>
    <section class="footer band-sky"></section>
  </main>
</body>
</html>
```